Marta Belcourt Name Card Design

Hello Designers,
I wanna have a name card with these details below:
Name: Marta Belcourt
Job Title: Doctor
Address: 2318 Ferris Lane, Tacoma, WA, US
Phone: 8273360915
Slogan on card: Health care 24/7, Whenever you need, we're there!
I love yellows colors, red and white. It would be nice if my card would be designed with these colors.

```html
<!DOCTYPE html>
<html lang="en">
<head>
<meta charset="utf-8">
<title>Marta Belcourt – Name Card</title>
<link rel="stylesheet" href="https://fonts.googleapis.com/css2?family=Lato:ital,wght@0,400;0,700;1,400&family=Oswald:wght@400;500&display=swap">
<style>
  :root {
    --card-bg: #ffffff;
    --ink: #37474a;
    --ink-muted: #6e7f80;
    --band-red: #780000;
    --band-orange: #ff8c00;
    --slogan-ink: #ffffff;
  }
  html, body {
    margin: 0;
    padding: 0;
    overflow: hidden;
    background: var(--card-bg);
  }
  .card {
    position: relative;
    width: 1200px;
    height: 686px;
    background: var(--card-bg);
    overflow: hidden;
    font-family: "Lato", sans-serif;
    color: var(--ink);
  }
  .card > * { position: absolute; margin: 0; line-height: 1; }
  .holder-name {
    left: 43px;
    top: 45px;
    font-size: 50px;
    font-weight: 700;
  }
  .holder-title {
    left: 43px;
    top: 112px;
    font-size: 40px;
    font-style: italic;
    font-weight: 400;
    color: var(--ink-muted);
  }
  .slogan-band {
    left: 0;
    top: 207px;
    width: 1200px;
    height: 205px;
    background: var(--band-red);
    display: flex;
    align-items: center;
    justify-content: center;
  }
  .slogan {
    font-family: "Oswald", sans-serif;
    font-weight: 500;
    font-size: 57px;
    color: var(--slogan-ink);
    letter-spacing: 0.2px;
  }
  .accent-stripe {
    left: 0;
    top: 412px;
    width: 1200px;
    height: 24px;
    background: var(--band-orange);
  }
  .contact-line {
    left: 43px;
    font-size: 41px;
    font-weight: 400;
  }
  .contact-address { top: 544px; }
  .contact-phone { top: 595px; }
</style>
</head>
<body>
  <main class="card">
    <h1 class="holder-name">Marta Belcourt</h1>
    <p class="holder-title">Doctor</p>
    <div class="slogan-band">
      <p class="slogan">Health care 24/7, Whenever you need, we're there!</p>
    </div>
    <div class="accent-stripe"></div>
    <p class="contact-line contact-address">Address: 2318 Ferris Lane, Tacoma, WA, US</p>
    <p class="contact-line contact-phone">Phone: 8273360915</p>
  </main>
</body>
</html>
```